We need a complete design for our construction company KELSO CONSTRUCTION based in Auckland New Zealand, we need a logo, website, business card, vehicle design etc..
We are a mid to high-end construction company who work mostly on residential projects and some commercial.

What we want to see in the design;
Professional,
Architectural,
Simple,
Alternative,

We want the design to communicate professionalism, high quality wormanship and and quality service.

Target Market(s)

People looking for a quality building/ construction company

Industry/Entity Type

Construction Company

Contact Information for Business Card

KELSO CONSTRUCTION.co.nz
Remi Tulvane
remi@kelsoconstruction-example.co.nz
021 5870 463

Logo Text

KELSO CONSTRUCTION

Number of Pages Required

5+ page

Font styles to use
Sans Serif

Colors

Designer to choose colors to be used in the design.

Requirements
Must have
• Must appear high end, professional, quality, be simple, easy to use, give security to potential clients
Nice to have
• high-quality photos of our recent projects
• about us page
• blog page
• contact us page
• high quality content
Should not have
• should not be hard to use and have too much going on.

```html
<!DOCTYPE html>
<html lang="en">
<head>
<meta charset="utf-8">
<title>Kelso Construction</title>
<link href="https://fonts.googleapis.com/css2?family=Josefin+Sans:wght@400;600;700&family=Lato:wght@400;700&display=swap" rel="stylesheet">
<style>
:root{
  --navy:#0d4c7d;
  --navy-dark:#0a3d66;
  --light:#f3f3f3;
  --card:#e6e6e6;
  --ink:#2b2b2b;
  --white:#fff;
  --stars:#f2b01e;
}
*{margin:0;padding:0;box-sizing:border-box}
html,body{width:1200px;height:3879px;overflow:hidden}
body{font-family:'Lato',sans-serif;color:var(--ink);background:var(--white);position:relative}
.head{font-family:'Josefin Sans',sans-serif;font-weight:400;letter-spacing:1px}
section{position:absolute;left:0;width:1200px}
.abs{position:absolute}
.photo{position:absolute}
.btn{position:absolute;background:var(--navy);color:var(--white);font-size:13px;border-radius:17px;height:34px;width:150px;display:flex;align-items:center;justify-content:center}
.section-title{position:absolute;left:0;width:1200px;text-align:center;font-family:'Josefin Sans',sans-serif;font-size:28px;color:var(--ink);letter-spacing:1px}
.pager{position:absolute;font-size:13px;color:#555;display:flex;align-items:center;gap:6px}

/* hero */
.hero{top:0;height:678px;overflow:hidden}
.hero-photo{inset:0;background:
  linear-gradient(180deg,rgba(20,60,110,.28),rgba(20,60,110,.28)),
  linear-gradient(180deg,#6f93b8 0%,#8ea7bf 36%,#a3adb3 48%,#6c7478 62%,#4c5256 80%,#3a3e41 100%)}
.brand{top:38px;width:1200px;text-align:center;color:var(--white);font-size:36px}
.nav{top:98px;width:1200px;display:flex;justify-content:center;gap:22px;color:var(--white);font-size:13.5px}
.nav .active{border-bottom:2px solid var(--white);padding-bottom:4px}
.hero-line{top:292px;width:1200px;text-align:center;color:var(--white);font-size:28px;line-height:38px}
.hero .pager{color:var(--white)}

/* quote */
.quote{top:678px;height:160px;background:var(--navy)}
.quote h2{position:absolute;top:14px;width:1200px;text-align:center;color:var(--white);font-weight:700;font-size:31px;letter-spacing:1px}
.field{position:absolute;top:80px;height:42px;background:var(--white);border-radius:3px;font-size:12px;color:#555;padding:0 14px;display:flex;align-items:center}
.field.submit{background:#f1f1f1;justify-content:center;padding:0}

/* about */
.about{top:838px;height:377px}
.about h2{position:absolute;left:122px;top:103px;font-size:27px}
.about p{position:absolute;left:122px;width:420px;font-size:12px;line-height:17px;color:#333}
.about-photo{left:662px;top:62px;width:378px;height:274px;background:linear-gradient(180deg,#c9dcef 0%,#a9c2dc 40%,#7c8fa3 62%,#5a6570 82%,#6d7469 100%)}

/* services */
.services{top:1215px;height:254px;background:var(--light)}
.svc-row{position:absolute;top:130px;left:130px;width:960px;display:flex;justify-content:space-between}
.svc{width:120px;text-align:center;font-size:13.5px;color:#444}
.svc svg{display:block;margin:0 auto 10px}
.svc.active{color:var(--navy);border-bottom:3px solid var(--navy);padding-bottom:6px}
.svc-sep{width:1px;height:54px;background:#aaa;margin-top:8px}

/* feature */
.feature{top:1469px;height:326px;background:var(--navy)}
.feature-photo{left:0;top:0;width:553px;height:326px;background:linear-gradient(180deg,#c4d6dc 0%,#8fae9a 22%,#3f6b3a 45%,#5c7d3f 62%,#b69a3a 72%,#8a8676 86%,#9b978a 100%)}
.feature .edge{position:absolute;left:553px;top:0;width:14px;height:326px;background:#1b6aa6}
.feature h3{position:absolute;left:632px;top:78px;color:var(--white);font-size:27px}
.feature p{position:absolute;left:632px;top:128px;width:450px;color:var(--white);font-size:12px;line-height:16px}
.btn.white{background:var(--white);color:var(--ink)}

/* projects */
.projects{top:1795px;height:605px}
.filters{position:absolute;top:120px;width:1200px;display:flex;justify-content:center;gap:28px;font-size:13px;color:#555}
.filters .on{color:var(--navy);border-bottom:2px solid var(--navy);padding-bottom:4px}
.proj{position:absolute;top:176px;width:300px;height:300px}
.proj .overlay{position:absolute;inset:0;background:rgba(13,76,125,.85);color:var(--white);padding:20px 22px}

/* testimonials */
.testi{top:2400px;height:476px;background:var(--light)}
.tcard{position:absolute;top:145px;width:306px;height:183px;background:var(--card)}
.tcard.on{background:var(--navy);color:var(--white)}
.tcard .q{position:absolute;left:18px;top:22px;font-family:Georgia,serif;font-size:40px;font-weight:700;line-height:1}
.tcard .avatar{position:absolute;left:60px;top:-8px;width:80px;height:80px;border:2px solid var(--navy);background:linear-gradient(180deg,#e8e8e8 0%,#c9b8a6 45%,#7b6a5e 100%)}
.tcard.on .avatar{border-color:var(--white)}
.tcard .name{position:absolute;left:152px;top:22px;font-family:'Josefin Sans',sans-serif;font-size:18px}
.tcard .role{position:absolute;left:152px;top:44px;font-size:12px}
.tcard .stars{position:absolute;left:208px;top:44px;color:var(--stars);font-size:11px;letter-spacing:1px}
.tcard .txt{position:absolute;left:22px;top:100px;width:262px;font-size:12px;line-height:16px}
.tcard .more{position:absolute;left:22px;top:148px;font-size:12px}
.tcard.on::after{content:"";position:absolute;left:22px;bottom:-14px;border-left:14px solid var(--navy);border-bottom:14px solid transparent}

/* blogs */
.blogs{top:2876px;height:465px}
.bcard{position:absolute;top:144px;width:434px;height:171px;background:var(--card)}
.bcard .img{position:absolute;left:10px;top:10px;width:150px;height:151px}
.bcard h4{position:absolute;left:178px;top:22px;font-family:'Josefin Sans',sans-serif;font-weight:400;font-size:27px}
.bcard p{position:absolute;left:178px;top:62px;width:236px;font-size:12px;line-height:16px;color:#444}
.bcard .meta{position:absolute;left:178px;top:130px;font-size:12px;color:#444;display:flex;gap:14px}
.bcard .meta span+span{border-left:1px solid #888;padding-left:14px}

/* newsletter */
.news{top:3341px;height:223px;background:var(--light)}
.news-box{position:absolute;left:320px;top:106px;width:560px;height:52px;background:var(--white);border-radius:26px;font-size:12px;color:#aaa;padding:0 30px;display:flex;align-items:center}
.news-send{position:absolute;right:0;top:0;width:74px;height:52px;border-radius:26px;background:var(--navy);display:flex;align-items:center;justify-content:center}

/* footer */
.footer{left:0;width:1200px;top:3564px;height:315px;background:linear-gradient(180deg,#2e353b 0%,#262b30 55%,#1c2024 100%);color:var(--white)}
.footer h5{position:absolute;top:54px;font-family:'Josefin Sans',sans-serif;font-weight:400;font-size:17px;letter-spacing:.5px}
.footer .rule{position:absolute;top:80px;height:1px;background:#777}
.footer p,.footer li{font-size:12px;line-height:17px}
.footer ul{position:absolute;left:419px;top:96px;list-style:none}
.footer li::before{content:"▸ ";font-size:11px}
.contact-row{position:absolute;left:621px;display:flex;gap:12px;font-size:12px;align-items:flex-start}
.map{position:absolute;left:892px;top:96px;width:186px;height:108px;border:2px solid #ddd;background:
  radial-gradient(circle at 40% 55%,#f0d9a0 0 14%,transparent 30%),
  linear-gradient(135deg,#e4e8d6 0%,#cfdcea 45%,#a9c8e4 60%,#e9e1c9 100%)}
.social{position:absolute;top:266px;width:34px;height:34px;border-radius:50%;border:1.5px solid var(--white)}
</style>
</head>
<body>

<section class="hero">
  <div class="photo hero-photo" role="img" aria-label="City skyline with a tall tower under a blue sky"></div>
  <div class="abs head brand">KELSO CONSTRUCTION</div>
  <nav class="abs nav"><span class="active">Home</span><span>About</span><span>Services</span><span>Projects</span><span>Testimonial</span><span>Blogs</span><span>Contact</span></nav>
  <div class="abs head hero-line">WE ARE A MID TO HIGH-END<br>CONSTRUCTION COMPANY</div>
  <div class="btn" style="left:525px;top:384px">Read More</div>
  <div class="pager" style="left:36px;top:336px">&#8592; Prev.</div>
  <div class="pager" style="left:1110px;top:336px">Next &#8594;</div>
</section>

<section class="quote">
  <h2>GET A QUOTE</h2>
  <div class="field" style="left:124px;width:264px">Name</div>
  <div class="field" style="left:403px;width:264px">E-Mail</div>
  <div class="field" style="left:680px;width:264px">Phone Number</div>
  <div class="field submit" style="left:965px;width:113px">GET A QUOTE</div>
</section>

<section class="about">
  <h2 class="head">ABOUT KELSO</h2>
  <p style="top:155px">Lorem Ipsum is simply dummy text of the printing and typesetting industry.</p>
  <p style="top:202px">Lorem Ipsum is simply dummy text of the printing and typesetting industry.</p>
  <div class="btn" style="left:122px;top:260px">Read More</div>
  <div class="photo about-photo" role="img" aria-label="Modern high-rise buildings with a construction crane"></div>
</section>

<section class="services">
  <div class="section-title" style="top:72px">OUR SERVICES</div>
  <div class="svc-row">
    <div class="svc active"><svg width="40" height="36" viewBox="0 0 40 36" fill="none" stroke="#0d4c7d" stroke-width="2"><path d="M4 30h32M8 30l6-12h10l4 8M14 18l6-10 10 6"/><circle cx="12" cy="31" r="2"/><circle cx="28" cy="31" r="2"/></svg>Construction</div>
    <div class="svc-sep"></div>
    <div class="svc"><svg width="40" height="36" viewBox="0 0 40 36" fill="none" stroke="#444" stroke-width="2"><rect x="8" y="4" width="22" height="8"/><path d="M30 8h4v8H20v6M20 22v10"/></svg>Tiling &amp; painting</div>
    <div class="svc-sep"></div>
    <div class="svc"><svg width="40" height="36" viewBox="0 0 40 36" fill="none" stroke="#444" stroke-width="2"><path d="M6 18L20 6l14 12M10 15v17h20V15"/><rect x="17" y="22" width="6" height="10"/></svg>Renovation</div>
    <div class="svc-sep"></div>
    <div class="svc"><svg width="40" height="36" viewBox="0 0 40 36" fill="none" stroke="#444" stroke-width="2"><rect x="8" y="10" width="20" height="22"/><path d="M12 16h4M20 16h4M12 22h4M20 22h4M28 6l6 6-8 8"/></svg>Design &amp; Build</div>
    <div class="svc-sep"></div>
    <div class="svc"><svg width="40" height="36" viewBox="0 0 40 36" fill="none" stroke="#444" stroke-width="2"><path d="M26 4l6 6-18 18-8 2 2-8z"/></svg>Consulting</div>
    <div class="svc-sep"></div>
    <div class="svc"><svg width="40" height="36" viewBox="0 0 40 36" fill="none" stroke="#444" stroke-width="2"><circle cx="20" cy="18" r="6"/><circle cx="20" cy="18" r="13" stroke-dasharray="4 3"/></svg>Management</div>
    <div class="svc-sep"></div>
    <div class="svc"><svg width="40" height="36" viewBox="0 0 40 36" fill="none" stroke="#444" stroke-width="2"><rect x="8" y="4" width="24" height="28"/><path d="M8 16h12v16M20 10h12"/></svg>Floor Planning</div>
  </div>
</section>

<section class="feature">
  <div class="photo feature-photo" role="img" aria-label="Yellow excavator on a site surrounded by trees"></div>
  <div class="edge"></div>
  <h3 class="head">CONSTRUCTION</h3>
  <p>Lorem Ipsum is simply dummy text of the printing and typesetting industry. Lorem Ipsum has been the industry's standard dummy text ever since the 1500s, when an unknown printer took a galley of type and scrambled it to make a type specimen book.</p>
  <div class="btn white" style="left:632px;top:241px">Read More</div>
</section>

<section class="projects">
  <div class="section-title" style="top:52px">OUR PROJECTS</div>
  <div class="filters"><span class="on">All</span><span>Architecture</span><span>Residential</span><span>Commercial</span><span>Renovation</span></div>
  <div class="proj" role="img" aria-label="Glass office building at sunset" style="left:0;background:linear-gradient(180deg,#4a6678 0%,#6b7f86 30%,#c08a42 55%,#6e5a34 72%,#2f3a26 100%)"></div>
  <div class="proj" role="img" aria-label="Two-storey family house" style="left:300px;background:linear-gradient(180deg,#dfe5ea,#8e9aa4)">
    <div class="overlay">
      <div class="head" style="font-size:17px">Loream Ipsum</div>
      <div style="font-size:12px;margin-top:4px">City,Country</div>
      <svg class="abs" style="left:134px;top:134px" width="32" height="32" viewBox="0 0 32 32" fill="none" stroke="#fff" stroke-width="2.5"><path d="M2 10V2h8M22 2h8v8M30 22v8h-8M10 30H2v-8"/></svg>
    </div>
  </div>
  <div class="proj" role="img" aria-label="Modern residential home with red panels" style="left:600px;background:linear-gradient(180deg,#d6e4ee 0%,#b9c7cf 25%,#b4533a 45%,#7f6a5c 62%,#9a9c9b 80%,#b7b9b7 100%)"></div>
  <div class="proj" role="img" aria-label="Curved glass tower against blue sky" style="left:900px;background:linear-gradient(160deg,#2a5c98 0%,#5c88bd 35%,#9dbbd9 65%,#dfe8f1 100%)"></div>
  <div class="pager" style="left:36px;top:318px;color:#fff">&#8592; Prev.</div>
  <div class="pager" style="left:1110px;top:318px;color:#fff">Next &#8594;</div>
  <div class="btn" style="left:525px;top:523px">View More</div>
</section>

<section class="testi">
  <div class="section-title" style="top:50px">TESTIMONIALS</div>
  <div class="pager" style="left:36px;top:218px">&#8592; Prev.</div>
  <div class="pager" style="left:1110px;top:218px">Next &#8594;</div>
  <div class="tcard" style="left:122px">
    <div class="q">&ldquo;</div><div class="avatar" role="img" aria-label="Client portrait"></div>
    <div class="name">LIAM HARROW</div><div class="role">Client</div><div class="stars">★★★★★</div>
    <div class="txt">Lorem Ipsum is simply dummy text of the printing and typesetting industry.</div><div class="more">Read More...»</div>
  </div>
  <div class="tcard on" style="left:447px">
    <div class="q">&ldquo;</div><div class="avatar" role="img" aria-label="Client portrait"></div>
    <div class="name">OWEN TASKER</div><div class="role">Client</div><div class="stars">★★★★★</div>
    <div class="txt">Lorem Ipsum is simply dummy text of the printing and typesetting industry.</div><div class="more">Read More...»</div>
  </div>
  <div class="tcard" style="left:773px">
    <div class="q">&ldquo;</div><div class="avatar" role="img" aria-label="Client portrait"></div>
    <div class="name">NOAH VERRILL</div><div class="role">Client</div><div class="stars">★★★★★</div>
    <div class="txt">Lorem Ipsum is simply dummy text of the printing and typesetting industry.</div><div class="more">Read More...»</div>
  </div>
  <div class="btn" style="left:525px;top:389px">View More</div>
</section>

<section class="blogs">
  <div class="section-title" style="top:62px">OUR LATEST BLOGS</div>
  <div class="pager" style="left:36px;top:218px">&#8592; Prev.</div>
  <div class="pager" style="left:1110px;top:218px">Next &#8594;</div>
  <div class="bcard" style="left:124px">
    <div class="img" role="img" aria-label="Grey two-storey house" style="background:linear-gradient(180deg,#7fa6d2 0%,#aab7c4 35%,#8d9399 60%,#5f6b55 100%)"></div>
    <h4>Blog Title 1</h4>
    <p>Lorem Ipsum is simply dummy text of the printing and typesetting industry.</p>
    <div class="meta"><span>Mar.20.2018</span><span>12 Comments</span></div>
  </div>
  <div class="bcard" style="left:603px">
    <div class="img" role="img" aria-label="Ornate apartment building facade" style="background:linear-gradient(180deg,#b3cde6 0%,#c49a82 35%,#a45f48 60%,#5e463d 100%)"></div>
    <h4>Blog Title 2</h4>
    <p>Lorem Ipsum is simply dummy text of the printing and typesetting industry.</p>
    <div class="meta"><span>Mar.23.2018</span><span>14 Comments</span></div>
  </div>
  <div class="btn" style="left:525px;top:365px">View More</div>
</section>

<section class="news">
  <div class="section-title" style="top:52px">SUBSCRIBE TO OUR NEWS LETTER</div>
  <div class="news-box">Your E-Mail Here
    <div class="news-send"><svg width="22" height="22" viewBox="0 0 24 24" fill="#fff"><path d="M2 21l21-9L2 3v7l15 2-15 2z"/></svg></div>
  </div>
</section>

<footer class="abs footer">
  <h5 style="left:122px">KELSO CONSTRUCTION</h5><div class="rule" style="left:122px;width:150px"></div>
  <p class="abs" style="left:122px;top:96px;width:170px;letter-spacing:.6px">Lorem Ipsum is simply dummy text of the printing and typesetting industry.</p>
  <p class="abs" style="left:122px;top:188px">Read More... »</p>
  <h5 style="left:419px">QUICK LINK</h5><div class="rule" style="left:419px;width:150px"></div>
  <ul><li>Home</li><li>FAQ</li><li>Privacy&amp;Terms</li><li>Contact</li><li>Help</li></ul>
  <h5 style="left:621px">CONTACT US</h5><div class="rule" style="left:621px;width:230px"></div>
  <div class="contact-row" style="top:100px"><svg width="12" height="12" viewBox="0 0 24 24" fill="#fff"><path d="M6 2l4 5-2 3a12 12 0 006 6l3-2 5 4-3 4C10 22 2 14 2 5z"/></svg>021 5870 463</div>
  <div class="contact-row" style="top:130px"><svg width="12" height="12" viewBox="0 0 24 24" fill="none" stroke="#fff" stroke-width="3"><circle cx="12" cy="12" r="4"/><path d="M16 12v2a3 3 0 006 0v-2a10 10 0 10-4 8"/></svg>info@kelsoconstruction-example.co.nz</div>
  <div class="contact-row" style="top:160px"><svg width="12" height="14" viewBox="0 0 24 28" fill="#fff"><path d="M12 0a9 9 0 00-9 9c0 7 9 19 9 19s9-12 9-19a9 9 0 00-9-9zm0 13a4 4 0 110-8 4 4 0 010 8z"/></svg><span>48 Harbour Rd. Auckland,<br>NZ 1010</span></div>
  <h5 style="left:892px">LOCATION MAP</h5><div class="rule" style="left:892px;width:186px"></div>
  <div class="map" role="img" aria-label="Street map of the office location"></div>
  <div class="abs" style="left:122px;top:252px;width:956px;height:1px;background:#777"></div>
  <p class="abs" style="left:122px;top:274px">CopyRight © 2018 Kelso construction. All Right Reserve</p>
  <div class="social" style="left:964px" aria-label="Social link"></div>
  <div class="social" style="left:1004px" aria-label="Social link"></div>
  <div class="social" style="left:1044px" aria-label="Social link"></div>
</footer>

</body>
</html>
```